Lantern Quillhouse Website

Create website for Legal Management Company which specializes in Law Office Spersriinal Management
System implementation & Training
Global presence
Paralegal Services - Remote or In-Office
Legal Research
- Judge Motion Ruling History
- Opposing Counsel Opposition Research - Historical Filings - Pattern identification
Service by Mail - Ex- Parte Notice

Probate -Heir Finder - Asset Location -

```html
<!DOCTYPE html>
<html lang="en">
<head>
<meta charset="utf-8">
<title>Lantern Quillhouse — Legal Management</title>
<link href="https://fonts.googleapis.com/css2?family=Playfair+Display:ital,wght@0,400;1,400&family=Inter:wght@300;400;500;600&display=swap" rel="stylesheet">
<style>
:root{
  --ink:#0a0e19;
  --navy:#0c111e;
  --slate:#1f2739;
  --card:#0f1421;
  --black:#000;
  --gold:#c4a462;
  --white:#ffffff;
  --text:#c9cdd6;
  --muted:#8a909c;
  --faint:#5d6371;
  --line:#262c3a;
  --serif:'Playfair Display',Georgia,serif;
  --sans:'Inter',Helvetica,Arial,sans-serif;
}
*{box-sizing:border-box;margin:0;padding:0}
html,body{width:1200px;height:2955px;overflow:hidden;background:var(--ink);font-family:var(--sans);color:var(--white)}
section,footer{position:relative;width:1200px;overflow:hidden}
.abs{position:absolute}
.eyebrow{font-size:9.5px;letter-spacing:3.3px;color:var(--gold);font-weight:500;text-transform:uppercase}
.serif{font-family:var(--serif);font-weight:400}

/* hero */
.hero{height:910px;background:linear-gradient(180deg,#161a26 0%,#0b0f1b 100%)}
.hero-visual{left:597px;top:0;width:603px;height:910px;background:linear-gradient(200deg,#3a3d46 0%,#24272f 30%,#12151e 70%,#0b0f1b 100%)}
.hero-fade{left:0;top:0;width:1200px;height:910px;background:linear-gradient(90deg,#0d1120 0%,rgba(13,17,32,.9) 45%,rgba(13,17,32,.2) 100%)}
.brand{display:flex;align-items:center;gap:10px;font-size:15px;letter-spacing:4px;color:var(--white);font-weight:400}
.brand-box{width:28px;height:28px;border:1px solid var(--gold)}
.nav{left:632px;top:31px;display:flex;gap:36px;font-size:8.5px;letter-spacing:1.8px;font-weight:500}
.nav-cta{left:977px;top:22px;width:149px;height:29px;background:var(--gold);color:var(--ink);font-size:8.5px;letter-spacing:2px;font-weight:600;display:flex;align-items:center;justify-content:center}
.hero-eyebrow{left:72px;top:274px;display:flex;align-items:center;gap:14px}
.hero-eyebrow span.rule{width:34px;height:1px;background:var(--gold)}
.hero-title{left:72px;top:312px;font-size:97px;line-height:92px}
.hero-title em{color:var(--gold);font-style:italic;display:block}
.hero-copy{left:72px;top:531px;width:412px;font-size:15px;line-height:20.5px;color:var(--text);font-weight:300}
.btn{height:42px;display:flex;align-items:center;justify-content:center;font-size:9px;letter-spacing:1.6px;font-weight:600;gap:10px}
.btn-solid{left:72px;top:660px;width:162px;background:var(--white);color:var(--ink)}
.btn-ghost{left:252px;top:660px;width:189px;border:1px solid #4a4f5c;color:var(--white)}

/* operations */
.ops{height:475px;background:var(--ink)}
.ops-title{left:72px;top:94px;font-size:37px;line-height:35px}
.ops-copy{left:72px;top:210px;width:330px;font-size:12px;line-height:19px;color:var(--muted)}
.feature{left:72px;display:flex;gap:14px;align-items:center}
.feature .ico{width:35px;height:35px;border:1px solid var(--line);display:flex;align-items:center;justify-content:center}
.feature b{display:block;font-size:10.5px;letter-spacing:.8px;font-weight:600}
.feature small{display:block;font-size:8.5px;color:var(--faint);margin-top:3px}
.svc{background:var(--card);border:1px solid #1b2130;width:331px}
.svc .tag{position:absolute;right:36px;top:38px;font-size:7px;letter-spacing:1.2px;color:var(--faint)}
.svc .icon{position:absolute;left:36px;top:36px}
.svc h3{position:absolute;left:36px;top:102px;font-family:var(--serif);font-weight:400;font-size:18px}
.svc p{position:absolute;left:36px;top:142px;width:262px;font-size:10.5px;line-height:16.5px;color:var(--muted)}
.svc ul{position:absolute;left:36px;top:212px;list-style:none;font-size:9px;line-height:20.5px;color:var(--text)}
.svc li::before{content:"";display:inline-block;width:3px;height:3px;background:var(--gold);margin-right:6px;vertical-align:middle}

/* intelligence */
.intel{height:675px;background:var(--slate)}
.intel-head{left:0;width:1200px;text-align:center}
.intel-title{top:138px;font-size:46px;line-height:44px}
.intel-card{top:299px;width:509px;height:282px;background:var(--ink);border:1px solid #0a0d16;box-shadow:inset 0 0 0 2px #141a28}
.intel-card .kicker{position:absolute;left:39px;top:40px;font-family:var(--serif);font-style:italic;font-size:15px;color:var(--gold)}
.intel-card .dot{position:absolute;right:39px;top:38px;width:23px;height:23px;border-radius:50%;border:1px solid var(--line);display:flex;align-items:center;justify-content:center}
.intel-card h3{position:absolute;left:39px;top:88px;font-weight:300;font-size:18px;letter-spacing:-.2px}
.intel-card p{position:absolute;left:39px;top:138px;width:432px;font-size:11.5px;line-height:19px;color:var(--muted)}
.intel-card .foot{position:absolute;left:39px;right:39px;border-top:1px solid var(--line);display:flex;justify-content:space-between;padding-top:17px;font-size:7.5px;letter-spacing:1.2px;color:var(--faint)}
.intel-card .foot a{color:var(--gold);font-size:9px;letter-spacing:0;font-weight:500;text-decoration:none}

/* practices */
.practice{height:430px;background:var(--navy)}
.practice-title{left:72px;top:178px;font-size:38px;line-height:36px;width:500px}
.practice-copy{left:72px;top:259px;width:490px;font-size:13px;line-height:22px;color:var(--muted)}
.stat{top:339px}
.stat b{display:block;font-family:var(--serif);font-weight:400;font-size:23px;color:var(--gold)}
.stat small{display:block;font-size:7.5px;letter-spacing:1.8px;color:var(--faint);margin-top:4px}
.hubs{left:629px;top:94px;width:497px;height:322px;border:1px solid #1e2434;background:linear-gradient(160deg,#10152297 0%,#111624 60%,#0e1320 100%)}
.hub-row{position:absolute;left:47px;right:47px;display:flex;justify-content:space-between;align-items:center;border-bottom:1px solid var(--line);padding-bottom:15px;font-size:14.5px;color:var(--text);font-weight:300}
.hub-row small{font-size:7.5px;color:var(--faint)}
.hubs-link{left:47px;top:263px;font-size:9px;letter-spacing:1.8px;color:var(--gold);font-weight:600;display:flex;align-items:center;gap:8px}

/* footer */
.site-footer{height:465px;background:var(--black)}
.foot-tag{left:72px;top:142px;font-size:23px;line-height:27px}
.foot-copy{left:72px;top:220px;font-size:9.5px;line-height:14.5px;color:var(--faint)}
.field{width:287px}
.field label{display:block;font-size:7.5px;letter-spacing:1.2px;color:var(--muted)}
.field .val{margin-top:24px;font-size:10.5px;padding-bottom:10px;border-bottom:1px solid #2a2f3a}
.field.active .val{border-bottom-color:var(--gold)}
.submit{left:530px;top:280px;width:596px;height:42px;border:1.5px solid var(--gold);color:var(--gold);font-size:8.5px;letter-spacing:3.4px;font-weight:600;display:flex;align-items:center;justify-content:center}
.legal{left:72px;right:74px;top:425px;display:flex;justify-content:space-between;font-size:7.5px;letter-spacing:1.6px;color:var(--faint)}
.legal nav{display:flex;gap:42px}
</style>
</head>
<body>

<section class="hero">
  <div class="abs hero-visual" role="img" aria-label="Dark photograph of glass skyscrapers seen from below"></div>
  <div class="abs hero-fade"></div>
  <div class="abs brand" style="left:72px;top:22px"><span class="brand-box"></span>LANTERN QUILLHOUSE</div>
  <nav class="abs nav"><span>SOLUTIONS</span><span>INTELLIGENCE</span><span>GLOBAL PRESENCE</span></nav>
  <div class="abs nav-cta">CONTACT PARTNER</div>
  <div class="abs hero-eyebrow eyebrow"><span class="rule"></span>Architects of Law Practice</div>
  <h1 class="abs hero-title serif">Precision<em>Redefined.</em></h1>
  <p class="abs hero-copy">Elevating legal operations through tailored management, judicial intelligence, and seamless global infrastructure. We don’t just manage firms; we engineer their competitive advantage.</p>
  <div class="abs btn btn-solid">OUR METHODOLOGY</div>
  <div class="abs btn btn-ghost">LEGAL INTELLIGENCE
    <svg width="8" height="8" viewBox="0 0 8 8"><path d="M2.5 1l3 3-3 3" fill="none" stroke="#fff" stroke-width="1.2"/></svg></div>
</section>

<section class="ops">
  <div class="abs eyebrow" style="left:72px;top:50px">Operational Excellence</div>
  <h2 class="abs ops-title serif">System<br>Implementation &amp;<br>Elite Training</h2>
  <p class="abs ops-copy">Transition your practice into a high-performance machine. We implement industry-leading legal tech stacks and provide hands-on training for your entire team.</p>
  <div class="abs feature" style="top:294px">
    <span class="ico"><svg width="16" height="14" viewBox="0 0 16 14"><rect x="1" y="1" width="14" height="9" rx="1" fill="none" stroke="#c4a462" stroke-width="1.2"/><path d="M5 13h6M8 10v3" stroke="#c4a462" stroke-width="1.2"/></svg></span>
    <div><b>CUSTOM STACK AUDIT</b><small>Tailored software selection for your specific caseload.</small></div>
  </div>
  <div class="abs feature" style="top:346px">
    <span class="ico"><svg width="16" height="14" viewBox="0 0 16 14"><circle cx="6" cy="4" r="2.6" fill="none" stroke="#c4a462" stroke-width="1.2"/><path d="M1 13c0-3 2.3-5 5-5s5 2 5 5M11 1.5a2.6 2.6 0 010 5M13 8.5c1.3.8 2 2.5 2 4.5" fill="none" stroke="#c4a462" stroke-width="1.2"/></svg></span>
    <div><b>BESPOKE TRAINING</b><small>On-site or remote workshops for partners and staff.</small></div>
  </div>

  <article class="abs svc" style="left:439px;top:49px;height:331px">
    <svg class="icon" width="28" height="24" viewBox="0 0 28 24"><rect x="1.5" y="6" width="25" height="16.5" rx="2" fill="none" stroke="#c4a462" stroke-width="1.8"/><path d="M9 6V2.5h10V6M9 6v16.5M19 6v16.5" fill="none" stroke="#c4a462" stroke-width="1.8"/></svg>
    <span class="tag">STRATEGIC SUPPORT</span>
    <h3>Paralegal Services</h3>
    <p>Agile support that scales with your trial schedule. Whether in-office for high-volume filing or remote for document review.</p>
    <ul><li>Multi-state Support</li><li>Remote Discovery Management</li><li>On-site Trial Support</li></ul>
  </article>

  <article class="abs svc" style="left:794px;top:84px;height:296px">
    <svg class="icon" width="28" height="22" viewBox="0 0 28 22"><rect x="1.5" y="1.5" width="25" height="19" rx="2" fill="none" stroke="#c4a462" stroke-width="1.8"/><path d="M2 3l12 9 12-9" fill="none" stroke="#c4a462" stroke-width="1.8"/></svg>
    <span class="tag">SPECIALIZED NOTICE</span>
    <h3>Service by Mail</h3>
    <p>Precision delivery for sensitive legal matters. Specialized in Ex-Parte notice requirements and high-priority legal communications.</p>
    <ul><li>Certified Compliance Tracking</li><li>Ex-Parte Notice Specialists</li><li>International Service Support</li></ul>
  </article>
</section>

<section class="intel">
  <div class="abs intel-head eyebrow" style="top:95px">Strategic Intelligence</div>
  <h2 class="abs intel-head intel-title serif">Know the Bench.<br>Predict the Room.</h2>

  <article class="abs intel-card" style="left:72px">
    <span class="kicker">Judge Analytics</span>
    <span class="dot"><svg width="10" height="10" viewBox="0 0 10 10"><circle cx="4.2" cy="4.2" r="3" fill="none" stroke="#fff" stroke-width="1"/><path d="M6.5 6.5L9 9" stroke="#fff" stroke-width="1"/></svg></span>
    <h3>MOTION RULING HISTORY</h3>
    <p>Data-driven profiles of specific judges. We analyze historical ruling patterns for summary judgments, discovery disputes, and evidentiary motions to inform your strategy.</p>
    <div class="foot" style="top:214px"><span>PREDICTIVE MODELING</span><a>Request Case Study</a></div>
  </article>

  <article class="abs intel-card" style="left:616px">
    <span class="kicker">Opposition Intel</span>
    <span class="dot"><svg width="10" height="10" viewBox="0 0 10 10"><circle cx="5" cy="5" r="4" fill="none" stroke="#fff" stroke-width="1"/><circle cx="5" cy="5" r="1.6" fill="none" stroke="#fff" stroke-width="1"/></svg></span>
    <h3>COUNSEL PATTERN IDENTIFICATION</h3>
    <p>Exhaustive opposition research. We track historical filings of opposing counsel to identify tactical repetitions, common pitfalls, and negotiation pressure points.</p>
    <div class="foot" style="top:195px"><span>TACTICAL ADVANTAGE</span><a>Access Portal</a></div>
  </article>
</section>

<section class="practice">
  <div class="abs eyebrow" style="left:72px;top:138px">Specialized Practices</div>
  <h2 class="abs practice-title serif">Probate, Heir Hunting &amp; Asset Recovery</h2>
  <p class="abs practice-copy">Complex estates require specialized forensics. Our investigative team excels in identifying missing heirs and locating hidden assets across jurisdictions.</p>
  <div class="abs stat" style="left:72px"><b>98%</b><small>ASSET RECOVERY SUCCESS</small></div>
  <div class="abs stat" style="left:332px"><b>Global</b><small>INVESTIGATION NETWORK</small></div>

  <div class="abs hubs" role="img" aria-label="Global hubs panel over a faint world map texture">
    <div class="abs eyebrow" style="left:47px;top:48px">Global Hubs</div>
    <div class="hub-row" style="top:78px">New York<small>Corporate HQ</small></div>
    <div class="hub-row" style="top:135px">London<small>EU Operations</small></div>
    <div class="hub-row" style="top:191px">Singapore<small>APAC Support</small></div>
    <div class="abs hubs-link">VIEW NETWORK
      <svg width="9" height="8" viewBox="0 0 9 8"><path d="M0 4h8M5 1l3 3-3 3" fill="none" stroke="#c4a462" stroke-width="1.2"/></svg></div>
  </div>
</section>

<footer class="site-footer">
  <div class="abs brand" style="left:72px;top:86px;font-size:14px;gap:10px"><span class="brand-box" style="width:23px;height:23px"></span>LANTERN QUILLHOUSE</div>
  <p class="abs foot-tag serif">Elevate your practice.<br>Secure your edge.</p>
  <p class="abs foot-copy">The intersection of operational mastery and litigation intelligence.<br>Contact us to schedule a confidential firm audit.</p>

  <div class="abs field active" style="left:530px;top:94px"><label>NAME</label><div class="val">Miriam Ashcombe</div></div>
  <div class="abs field" style="left:839px;top:94px"><label>FIRM / COMPANY</label><div class="val">Harrowgate Counsel LLP</div></div>
  <div class="abs field" style="left:530px;top:180px;width:596px"><label>INQUIRY TYPE</label><div class="val">System Implementation</div></div>
  <div class="abs submit">INITIATE CONSULTATION</div>

  <div class="abs legal"><span>© 2024 LANTERN QUILLHOUSE. ALL RIGHTS RESERVED.</span><nav><span>TERMS</span><span>PRIVACY</span><span>FELLOWLINK</span></nav></div>
</footer>

</body>
</html>
```